Now hiring billboard for roofing company

We would like to design/slogan for a "now hiring" billboard for a variety of positions in our roofing company.
We perform residential and commercial roofing.
We are looking to hire roofers, laborers, gutter installers, sheet metal workers, commercial drivers, commercial roofers, and residential and commercial service technicians.
Looking to attract both entry level and experienced roofers.
Roofing is a good industry to build a career, learn a trade, we provide training.

Opportunity to learn a trade and move from unskilled to skilled positions.
Use Brantley Roofing as a stepping stone in your career.

Brantley Roofing is a stable, growing company that has been providing roofing services in the Portland area for over 35 years. We have a great team of employees, many with over 10 years with the company.
In addition to roofing homes, our Residential Department also offers repair and cleaning services as well as gutter installation and repair.
In 2014 we added a dedicated Commercial Department that services commercial customers with roofing projects and service/repairs. In addition, they offer the Brantley topGuard maintenance program.
Mostly recently Brantley Roofing purchased Voskuil Sheet Metal (VSM) in 2016. VSM specializes in custom metal fabrication, continuous gutters and custom copper fabrication.

If you are looking for a job where you are appreciated
at a company that values honesty and respect,
come and join our team!
Whether you are experienced or just wanting to
learn, we are looking to add hard-working, reliable
go-getters to our team. We offer a flexible work
environment and in addition to full-time work offer
part-time and summer positions.
We are always looking to add great people to our
team. Some of the job/career options are:
• Residential Roofer
• Commercial Roofer
• Gutter Installer
• Service Technician
• Sheet Metal Fabricator/Installer
• Commercial Driver
• General Labor

Brantley Roofing offers competitive pay and an excellent benefits package.

Join our team today!

Target Market(s)

Job seekers

Font styles to use
Serif

Colors

Designer to choose colors to be used in the design.

Requirements
Must have
• Get across that we are hiring and have our contact info
• CCB #62813
• brantleywork.example
Nice to have
• Simple, easy to understand regardless of language literacy.
• Have a high proportion of Hispanic workers, maybe include Spanish.
• Spanish hiring phone number is 503-555-0187

```html
<!DOCTYPE html>
<html lang="en">
<head>
<meta charset="utf-8">
<title>Brantley Roofing – Now Hiring Billboard</title>
<link href="https://fonts.googleapis.com/css2?family=Open+Sans:wght@400;600;700;800&family=Fira+Sans+Condensed:wght@400;500;600;700&display=swap" rel="stylesheet">
<style>
  :root {
    --orange: #f58a20;
    --navy: #34466f;
    --navy-dark: #2b3a5e;
    --ink: #2e3550;
    --grey: #4d5160;
    --white: #ffffff;
    --stage: #ece8e1;
    --sky-top: #eaf3fb;
    --sky-mid: #a9cdee;
    --roof: #9a6250;
  }
  * { margin: 0; padding: 0; box-sizing: border-box; }
  html, body { width: 912px; height: 1200px; overflow: hidden; background: var(--stage); }
  .stage { position: relative; width: 912px; height: 1200px; }
  .billboard {
    position: absolute; left: 26px; top: 420px;
    width: 1020px; height: 428px;
    transform: scale(0.8431); transform-origin: top left;
    background: var(--white); overflow: hidden;
    box-shadow: 0 4px 14px rgba(0,0,0,.18);
    font-family: "Open Sans", sans-serif;
  }
  .photo-crew {
    position: absolute; left: 0; top: 0; width: 480px; height: 428px;
    background: linear-gradient(180deg, var(--white) 0%, var(--sky-top) 18%, var(--sky-mid) 45%, #c8a58a 52%, var(--roof) 70%, #7e4e40 100%);
  }
  .shapes { position: absolute; inset: 0; }
  .brand { position: absolute; left: 70px; top: 40px; }
  .brand-name {
    font-family: "Fira Sans Condensed", sans-serif; font-weight: 700;
    font-size: 46px; color: var(--orange); line-height: 1; letter-spacing: -0.5px;
  }
  .brand-licence {
    font-family: "Fira Sans Condensed", sans-serif; font-weight: 500;
    font-size: 19px; color: var(--navy); text-align: right; margin-top: 6px;
  }
  .intro { position: absolute; right: 22px; top: 18px; width: 520px; text-align: right; }
  .tag-if {
    display: inline-block; background: var(--navy); color: var(--white);
    font-weight: 600; font-size: 25px; line-height: 32px; padding: 0 14px 0 16px;
    border-left: 6px solid var(--orange); letter-spacing: 1px;
  }
  .headline {
    font-weight: 700; font-size: 50px; line-height: 52px; color: var(--orange);
    letter-spacing: 1px; white-space: nowrap;
  }
  .subline { font-weight: 600; font-size: 12.5px; color: var(--ink); margin-top: 4px; white-space: nowrap; }
  .join { font-weight: 600; font-size: 22px; color: var(--ink); line-height: 26px; }
  .join span { color: var(--orange); font-weight: 700; }
  .pitch { font-size: 12.3px; color: var(--grey); line-height: 16px; margin-top: 6px; }
  .options-band {
    position: absolute; right: 26px; top: 218px; text-align: right;
    font-size: 12px; line-height: 17px; color: var(--white); white-space: nowrap;
  }
  .options-band strong { display: block; color: var(--orange); font-size: 14px; font-weight: 700; }
  .offer { position: absolute; left: 440px; top: 277px; width: 140px; text-align: center; color: var(--white); }
  .offer-title { font-family: "Fira Sans Condensed", sans-serif; font-weight: 700; font-size: 20px; color: var(--navy-dark); white-space: nowrap; }
  .offer-text { font-size: 10px; font-weight: 700; line-height: 12.5px; margin-top: 3px; }
  .jobs {
    position: absolute; top: 268px; list-style: none;
    font-family: "Fira Sans Condensed", sans-serif; font-weight: 500;
    font-size: 15.5px; line-height: 22.5px; color: var(--white); text-align: right;
    white-space: nowrap;
  }
  .jobs li::after { content: " •"; }
  .jobs-a { left: 585px; width: 150px; }
  .jobs-b { right: 26px; width: 260px; }
  .contact {
    position: absolute; left: 398px; right: 22px; top: 374px; height: 50px;
    display: flex; align-items: center; color: var(--white);
    font-family: "Fira Sans Condensed", sans-serif; white-space: nowrap;
  }
  .contact-note { font-size: 12.5px; line-height: 15px; flex-shrink: 0; }
  .divider { width: 1px; height: 32px; background: var(--white); margin: 0 9px; flex-shrink: 0; }
  .phone { font-size: 18px; font-weight: 600; display: flex; align-items: center; gap: 5px; flex-shrink: 0; }
  .phone em { font-style: normal; color: var(--orange); font-weight: 500; }
  .web { font-size: 18px; font-weight: 500; display: flex; align-items: center; gap: 6px; flex-shrink: 0; margin-left: auto; }
</style>
</head>
<body>
<main class="stage">
  <section class="billboard">
    <div class="photo-crew" role="img" aria-label="Photo of two roofers working on a shingled roof under a blue sky"></div>

    <svg class="shapes" width="1020" height="428" viewBox="0 0 1020 428">
      <polygon points="432,0 1020,0 1020,428 395,428 495,140" fill="#ffffff"/>
      <polygon points="375,0 432,0 495,140 395,428 380,428 480,140" fill="#f58a20"/>
      <polygon points="590,215 1020,215 1020,258 572,258" fill="#f58a20"/>
      <polygon points="605,215 1020,215 1020,258 587,258" fill="#34466f"/>
      <polygon points="433,262 1020,262 1020,366 390,366" fill="#f58a20"/>
      <line x1="598" y1="272" x2="598" y2="358" stroke="#ffffff" stroke-width="1" stroke-dasharray="2 3"/>
      <polygon points="388,370 1020,370 1020,428 362,428" fill="#34466f"/>
    </svg>

    <div class="brand">
      <div class="brand-name">Brantley Roofing</div>
      <div class="brand-licence">CCB #62813</div>
    </div>

    <header class="intro">
      <div class="tag-if">IF YOU ARE</div>
      <h1 class="headline">LOOKING FOR A JOB</h1>
      <p class="subline">WHERE YOU ARE APPRECIATED AT A COMPANY THAT VALUES HONESTY AND RESPECT,</p>
      <p class="join">COME AND <span>JOIN OUR TEAM!</span></p>
      <p class="pitch">Whether you are experienced or just wanting to learn, we are looking to add hard-working, reliable go-getters to our team. We offer a flexible work environment and in addition to full-time work offer part-time and summer positions.</p>
    </header>

    <div class="options-band">
      WE ARE ALWAYS LOOKING TO ADD GREAT PEOPLE TO OUR TEAM
      <strong>SOME OF THE JOB/CAREER OPTIONS ARE:</strong>
    </div>

    <div class="offer">
      <div class="offer-title">WE OFFERING</div>
      <p class="offer-text">COMPETITIVE PAY AND<br>AN EXCELLENT<br>BENEFITS PACKAGE.</p>
    </div>

    <ul class="jobs jobs-a">
      <li>Residential Roofer</li>
      <li>Commercial Roofer</li>
      <li>Gutter Installer</li>
      <li>General Labor</li>
    </ul>
    <ul class="jobs jobs-b">
      <li>Service Technician</li>
      <li>Sheet Metal Fabricator/Installer</li>
      <li>Commercial Driver</li>
      <li>Spanish/English Opportunities</li>
    </ul>

    <footer class="contact">
      <p class="contact-note">GET ACROSS THAT WE ARE HIRING<br>AND HAVE OUR CONTACT INFO</p>
      <span class="divider"></span>
      <span class="phone">
        <svg width="17" height="17" viewBox="0 0 24 24" aria-hidden="true"><path d="M6.6 10.8a15 15 0 0 0 6.6 6.6l2.2-2.2a1 1 0 0 1 1-.25 11.4 11.4 0 0 0 3.6.57 1 1 0 0 1 1 1V20a1 1 0 0 1-1 1A17 17 0 0 1 3 4a1 1 0 0 1 1-1h3.5a1 1 0 0 1 1 1c0 1.25.2 2.45.57 3.6a1 1 0 0 1-.25 1z" fill="#f58a20"/></svg>
        <span>503-555-0187</span> <em>(Spanish)</em>
      </span>
      <span class="divider"></span>
      <span class="web">
        <svg width="15" height="15" viewBox="0 0 16 16" aria-hidden="true"><circle cx="8" cy="8" r="7" fill="none" stroke="#f58a20" stroke-width="1.6"/><ellipse cx="8" cy="8" rx="3" ry="7" fill="none" stroke="#f58a20" stroke-width="1.2"/><line x1="1" y1="8" x2="15" y2="8" stroke="#f58a20" stroke-width="1.2"/></svg>
        brantleywork.example
      </span>
    </footer>
  </section>
</main>
</body>
</html>
```